BOX DESIGN OF CANINE AND FELINE RAPID TEST with PROFESSIONAL USE

"The market is in Southeast Asia, South America, Europe, and the U.S." Clients: Veterinary clinics, pet hospitals,(a small number of home use)
Positioned as a budget-friendly yet high-performance choice
Primary colors:
Green,Orange or Blue, (select 1,or 2 color)
Neutrals: Gray, Black or White (optional)
Dimensions:158mm(L)*98mm(W)*80mm(W)

Target Market(s)

Southeast Asia, South America, Europe, and the U.S.

Colors
0054AA
0677BA
7BADD7
CADEEF
E8F1F8
0094D4
00A9DD
6FCCEA
C7EBF8
E9F6FB
00AB8E
00BBA5
67D7C9
C6EFE9
E9F9F6
59FF00
82FF00
B8FF75
E3FFCB
F4FFEA
FFC000
F8CF3A
FAE287
FDF2CF
FEFAEE
F0912C
F2A743
F7CA91
FBE8D2
FDF5EE
EE7325
F08F49
F5BC92
FAE3D3
FDF4ED

Requirements
Nice to have
• Have an attractive look and preferably have pictures of pets (or outline lines of cats and dogs)

```html
<!DOCTYPE html>
<html lang="en">
<head>
<meta charset="utf-8">
<title>PawSure Rapid Test Kit – Box Dieline</title>
<link rel="stylesheet" href="https://fonts.googleapis.com/css2?family=Anton&family=Bricolage+Grotesque:opsz,wght@12..96,700;12..96,800&family=Poppins:wght@400;500;600&display=swap">
<style>
  :root {
    --royal: #1B1FA6;
    --lime: #8CC63F;
    --ink: #111111;
    --paper: #ffffff;
    --line: #2b2b2b;
    --fur: #d7a465;
    --fur-light: #f1dcc0;
  }
  * { margin: 0; padding: 0; box-sizing: border-box; }
  html, body { width: 1200px; height: 742px; overflow: hidden; background: var(--paper); }
  .dieline { position: relative; width: 1200px; height: 742px; font-family: "Poppins", sans-serif; color: var(--ink); }
  .dieline svg.cut { position: absolute; inset: 0; }
  .abs { position: absolute; }
  .brand { font-family: "Bricolage Grotesque", sans-serif; font-weight: 800; color: var(--ink); letter-spacing: -0.2px; line-height: 1; }
  .brand-white { color: var(--paper); }
  .headline { font-family: "Bricolage Grotesque", sans-serif; font-weight: 800; color: var(--royal); line-height: 0.92; letter-spacing: -1px; }
  .photo { position: absolute; }
  /* front panel */
  .front-title { left: 114px; top: 186px; font-size: 46px; transform: scaleX(0.92); transform-origin: left; }
  .front-sub { left: 114px; top: 266px; font-family: "Poppins", sans-serif; font-weight: 600; font-size: 12.5px; color: var(--lime); letter-spacing: -0.3px; }
  .contents { left: 114px; top: 290px; font-size: 5.2px; line-height: 6.9px; list-style: none; }
  .contents li { padding-left: 8px; text-indent: -8px; }
  .storage { left: 114px; top: 330px; font-size: 5.2px; }
  .symbols { left: 114px; top: 341px; display: flex; gap: 9px; align-items: center; }
  .ivd { font-size: 5px; font-weight: 600; border: 0.8px solid var(--ink); padding: 0 2px; line-height: 7px; }
  .count-badge { left: 221px; top: 293px; width: 50px; height: 42px; background: var(--paper); border-radius: 50% 45% 50% 48%; font-family: "Bricolage Grotesque", sans-serif; font-weight: 800; font-size: 8px; line-height: 9px; padding: 14px 0 0 6px; }
  /* side panel 1 */
  .slogan { left: 114px; top: 390px; font-size: 28px; line-height: 30px; letter-spacing: -0.8px; }
  .features { left: 112px; top: 454px; display: flex; gap: 8px; }
  .feature { display: flex; flex-direction: column; align-items: center; font-size: 3.4px; line-height: 3.6px; text-align: center; color: #333; width: 34px; }
  .feature svg { margin-bottom: 2px; }
  .cert { left: 371px; top: 470px; font-family: "Anton", sans-serif; font-size: 7.5px; }
  /* blue info panel */
  .info { left: 425px; top: 385px; width: 210px; color: var(--paper); font-size: 3.8px; line-height: 5px; }
  .info h4 { font-size: 3.9px; font-weight: 500; }
  .info ul { list-style: none; }
  .info li::before { content: "› "; color: var(--lime); }
  .info-box { background: var(--lime); width: 130px; margin: 4px 0 5px -1px; padding: 3px 4px; font-size: 2.7px; line-height: 3.4px; }
  .info-box b { font-weight: 600; font-size: 3px; }
  .spine-name { left: 560px; top: 410px; width: 92px; font-size: 26px; transform: rotate(-90deg); transform-origin: center; text-align: center; }
  .info-foot { left: 425px; top: 464px; }
  .info-foot .brand { font-size: 12px; }
  .info-foot p { font-size: 2.8px; color: var(--paper); margin-top: 2px; }
  /* main front 2 */
  .kit-title { left: 639px; top: 392px; font-size: 31px; line-height: 30px; transform: scaleX(0.88); transform-origin: left; }
  .species-tag { left: 639px; top: 456px; width: 91px; height: 16px; background: var(--lime); color: var(--paper); font-weight: 500; font-size: 7.6px; line-height: 16px; text-align: center; }
  /* panel 4 */
  .caps-slogan { left: 950px; top: 430px; font-family: "Anton", sans-serif; color: var(--lime); font-size: 24px; line-height: 27px; letter-spacing: -0.2px; }
</style>
</head>
<body>
<div class="dieline">

  <svg class="cut" width="1200" height="742" viewBox="0 0 1200 742" aria-hidden="true">
    <rect x="414" y="360" width="211" height="129" fill="var(--royal)"/>
    <rect x="940" y="360" width="210" height="129" fill="var(--royal)"/>
    <g fill="none" stroke="var(--line)" stroke-width="0.6">
      <path d="M99,150 V130 Q99,103 126,103 H387 Q414,103 414,130 V150"/>
      <line x1="99" y1="150" x2="414" y2="150"/>
      <path d="M99,150 V360 M414,150 V360"/>
      <path d="M414,360 L420,353 V267 H590 Q610,267 612,290 L620,352 L625,360"/>
      <path d="M940,360 L946,352 L952,290 Q955,267 975,267 H1145 V352 L1150,360"/>
      <path d="M99,360 L52,363 V485 L99,489"/>
      <rect x="99" y="360" width="1051" height="129"/>
      <path d="M414,360 V489 M625,360 V489 M940,360 V489"/>
      <path d="M99,489 V640 H150 Q169,640 169,620 V594 H344 V620 Q344,640 362,640 H414 V489"/>
      <path d="M414,489 L520,558 V587 Q520,605 539,605 H625 V489"/>
      <path d="M625,489 L695,593 V622 Q695,640 714,640 H851 Q870,640 870,622 V593 L940,489"/>
      <path d="M940,489 V605 H1026 Q1045,605 1045,587 V558 L1150,489"/>
    </g>
  </svg>

  <!-- Front panel -->
  <div class="photo" role="img" aria-label="Green organic backdrop shape behind the pets" style="left:212px;top:214px;width:202px;height:146px;background:var(--lime);border-radius:60% 0 0 45% / 40% 0 0 60%;"></div>
  <div class="photo" role="img" aria-label="Photo of a golden retriever hugging a calico cat" style="left:240px;top:187px;width:174px;height:173px;background:radial-gradient(ellipse at 65% 40%, var(--fur) 0%, #c98f4e 45%, var(--fur-light) 80%, rgba(255,255,255,0) 100%);border-radius:45% 10% 0 30%;"></div>
  <div class="abs brand" style="left:114px;top:166px;font-size:14px;">PawSure</div>
  <h1 class="abs headline front-title">CANINE &amp;<br>FELINE</h1>
  <div class="abs front-sub">RAPID TEST KIT</div>
  <ul class="abs contents">
    <li>(1)&nbsp; Test Kits(Cassette,disposable<br>&nbsp;&nbsp;&nbsp;&nbsp;dropper,desiccant)</li>
    <li>(2)&nbsp; Assay buffer</li>
    <li>(3)&nbsp; Sterile swabs</li>
    <li>(4)&nbsp; Instruction manual.</li>
  </ul>
  <div class="abs storage">Store at 2~30c, Avoid direct sunlight</div>
  <div class="abs symbols">
    <span class="ivd">IVD</span>
    <svg width="16" height="10" viewBox="0 0 16 10" fill="none" stroke="#111" stroke-width="0.6"><path d="M4,9 L8,9 M8,1 V9 M8,1 L12,1"/></svg>
    <svg width="12" height="10" viewBox="0 0 12 10" fill="none" stroke="#111" stroke-width="0.6"><circle cx="6" cy="5" r="2"/><path d="M6,0 V2 M6,8 V10 M0,5 H3 M9,5 H12 M2,1 L4,3 M10,1 L8,3 M2,9 L4,7 M10,9 L8,7"/></svg>
    <svg width="13" height="9" viewBox="0 0 13 9" fill="none" stroke="#111" stroke-width="0.6"><path d="M1,2 L6,1 V8 L1,8 Z M6,1 L12,2 V8 L6,8"/></svg>
    <svg width="9" height="9" viewBox="0 0 9 9" fill="none" stroke="#111" stroke-width="0.6"><circle cx="4.5" cy="4.5" r="3.8"/><path d="M3,3 Q4.5,1.8 5.8,3 L3,6.4 H6"/></svg>
  </div>
  <div class="abs count-badge">10 Tests<br>/Box</div>

  <!-- Side panel: slogan -->
  <div class="photo" role="img" aria-label="Faint green hexagon molecule pattern" style="left:290px;top:362px;width:124px;height:126px;background:linear-gradient(200deg, rgba(140,198,63,0.22), rgba(140,198,63,0) 70%);"></div>
  <div class="abs brand" style="left:114px;top:374px;font-size:11px;">PawSure</div>
  <h2 class="abs headline slogan">Loved by Pets,<br>Trusted by Vets</h2>
  <div class="abs features">
    <div class="feature">
      <svg width="14" height="14" viewBox="0 0 14 14" fill="none" stroke="var(--lime)" stroke-width="1"><circle cx="7" cy="8" r="5.3"/><path d="M7,5 V8 H9 M5.5,1 H8.5"/></svg>
      RESULTS<br>IN 10 MIN
    </div>
    <div class="feature">
      <svg width="16" height="14" viewBox="0 0 16 14" fill="none" stroke="var(--lime)" stroke-width="1"><path d="M2,13 V7 L5,4 L7,7 H11 L13,3 L15,6 V13 M6,13 V10 M11,13 V10"/></svg>
      HEALTH CHECK FOR<br>DOG AND CAT
    </div>
    <div class="feature">
      <svg width="14" height="14" viewBox="0 0 14 14" fill="none" stroke="var(--lime)" stroke-width="1"><path d="M5,13 L3,8 L5,7 V2 Q6,1 7,2 V6 L11,7 Q12,8 11,11 L9,13 Z"/></svg>
      EASY TO<br>USE
    </div>
  </div>
  <div class="abs cert">ISO GMO</div>

  <!-- Blue info panel -->
  <div class="abs brand brand-white" style="left:425px;top:370px;font-size:11px;">PawSure</div>
  <div class="abs info">
    <h4>Fácil y Práctico:</h4>
    <ul>
      <li>Sin capacitación previa</li>
      <li>Suficientemente simple para Para uso en casa</li>
    </ul>
    <div class="info-box">
      <b>RÁPIDO Y EFICIENTE:</b><br>
      Resultados digitales en &lt;10 minutos<br>
      Desde inicio hasta resultado final<br>
      <b>PRECISO Y FIABLE:</b><br>
      Resultados rápidos y confiables con tecnología de<br>
      inmunocromatografía avanzada<br>
      Validado por clínicas veterinarias a nivel global
    </div>
    <h4>DETECCIÓN MULTIENFERMEDADES:</h4>
    <ul>
      <li>Evalúa múltiples patologías simultáneamente</li>
      <li>Ayudar a los dueños de mascotas a detectar problemas a tiempo</li>
    </ul>
  </div>
  <div class="abs brand brand-white spine-name">PawSure</div>
  <div class="abs info-foot">
    <div class="brand brand-white">PawSure</div>
    <p>Loved by Pets, Trusted by Vets</p>
  </div>

  <!-- Second main panel -->
  <div class="photo" role="img" aria-label="Faint green hexagon molecule pattern" style="left:800px;top:366px;width:140px;height:123px;background:linear-gradient(160deg, rgba(140,198,63,0.18), rgba(140,198,63,0) 70%);"></div>
  <div class="photo" role="img" aria-label="Photo of a happy brown and white dog with its tongue out" style="left:826px;top:366px;width:112px;height:123px;background:radial-gradient(ellipse at 50% 45%, #f4ece3 0%, #d9894a 45%, #efe6dc 75%, rgba(255,255,255,0) 100%);border-radius:40% 40% 0 0;"></div>
  <div class="abs brand" style="left:639px;top:370px;font-size:11px;">PawSure</div>
  <h2 class="abs headline kit-title">PET RAPID<br>TEST KIT</h2>
  <div class="abs species-tag">FOR DOGS &amp; CATS</div>

  <!-- Blue slogan panel -->
  <div class="abs caps-slogan">LOVED BY PETS,<br>TRUSTED BY VETS</div>

</div>
</body>
</html>
```